Desktop and Mobile Site Homepage Redesign

We need a new website homepage redesign for www.plomzar.com. Plomzar is a new startup company based in San Francisco. We develop innovative iPhone application for consumers.
Our initial product is Plomzar that connects tv audiences with their favorite tv shows and fans. We would like to see designs that use the color red. The final design should communicate fun entertainment with social aspects relevant to USA cable tv shows.

We need 1. Desktop website and 2. Mobile website

Target Market(s)

USA

Industry/Entity Type

Entertainment

Number of Pages Required

2 page

Requirements
Must have
• Company name and logo. 1 Page Desktop View and 1 Page Mobile View.
Nice to have
• Details visit www.plomzar.com

```html
<!DOCTYPE html>
<html lang="en">
<head>
<meta charset="utf-8">
<title>Plomzar — Social Television</title>
<link rel="stylesheet" href="https://fonts.googleapis.com/css2?family=Source+Sans+3:wght@400;600;700;900&display=swap">
<style>
  :root {
    --red: #db1d18;
    --red-deep: #b3120f;
    --black: #000000;
    --charcoal: #202020;
    --white: #ffffff;
    --ink: #0c0c0c;
  }
  * { box-sizing: border-box; margin: 0; padding: 0; }
  html, body { width: 1200px; height: 2284px; overflow: hidden; }
  body { font-family: "Source Sans 3", Arial, sans-serif; background: var(--white); position: relative; }

  .hero { position: absolute; left: 0; top: 0; width: 1200px; height: 513px;
    background: linear-gradient(120deg, var(--red) 0%, #d01a15 55%, var(--red-deep) 100%); }
  .hero-phone { position: absolute; left: 678px; top: 0; width: 388px; height: 513px;
    background: linear-gradient(180deg, #f2f2f2 0%, #e2e2e2 55%, #e7b8a8 100%); border-radius: 28px 28px 0 0; }
  .brand { position: absolute; display: flex; align-items: center; gap: 12px; color: var(--white);
    font-weight: 400; font-size: 50px; line-height: 1; }
  .brand-dot { width: 22px; height: 22px; border-radius: 50%; background: var(--white); }
  .hero .brand { left: 120px; top: 108px; }
  .hero-title { position: absolute; left: 120px; top: 200px; color: var(--white); font-size: 40px; font-weight: 400; }
  .hero-sub { position: absolute; left: 120px; top: 250px; color: var(--white); font-size: 20px; font-weight: 700; }
  .hero-actions { position: absolute; left: 120px; top: 320px; display: flex; align-items: center; gap: 20px; }
  .btn-outline { display: inline-flex; align-items: center; justify-content: center; width: 146px; height: 37px;
    border: 2px solid var(--white); color: var(--white); font-size: 18px; font-weight: 700; }
  .link-signup { color: var(--white); font-size: 18px; font-weight: 700; }

  .tagline { position: absolute; left: 0; top: 513px; width: 1200px; height: 174px; background: var(--black);
    color: var(--white); font-size: 29px; font-weight: 600; display: flex; align-items: center; justify-content: center; }

  .feature { position: absolute; left: 120px; width: 960px; height: 196px; display: flex; align-items: center; }
  .feature-media { width: 390px; height: 196px; flex: none; }
  .feature-text { margin-left: 18px; }
  .feature-title { font-size: 40px; font-weight: 900; color: var(--ink); line-height: 1.05; }
  .feature-sub { font-size: 23px; font-weight: 600; color: var(--red); }
  .m1 { background: linear-gradient(135deg, #2a1410, #8a2a14 50%, #1c0d0a); }
  .m2 { background: linear-gradient(180deg, #e9e9e9, #cfcfcf 55%, #f3f3f3); }
  .m3 { background: linear-gradient(135deg, #3a2e28, #8d7a6a 55%, #d9d9d9); }
  .m4 { background: linear-gradient(180deg, #f1f1f1, #c9cbcc 60%, #8e9194); }

  .invite { position: absolute; left: 0; top: 1628px; width: 1200px; height: 343px;
    background: linear-gradient(180deg, #252525, var(--charcoal)); color: var(--white); text-align: center; }
  .invite-title { position: absolute; left: 0; right: 0; top: 60px; font-size: 42px; font-weight: 600; }
  .invite-sub { position: absolute; left: 0; right: 0; top: 136px; font-size: 24px; font-weight: 700; }
  .btn-solid { position: absolute; left: 498px; top: 209px; width: 204px; height: 62px; background: var(--red);
    color: var(--white); font-size: 26px; font-weight: 700; display: flex; align-items: center; justify-content: center; }

  .footer { position: absolute; left: 0; top: 1971px; width: 1200px; height: 313px; background: var(--red); color: var(--white); }
  .footer .brand { left: 120px; top: 50px; }
  .footer-address { position: absolute; left: 120px; top: 116px; font-size: 20px; font-weight: 600; }
  .footer-email { position: absolute; left: 120px; top: 158px; font-size: 20px; font-weight: 600; }
  .newsletter-label { position: absolute; left: 691px; top: 40px; font-size: 20px; font-weight: 600; }
  .newsletter { position: absolute; left: 691px; top: 74px; display: flex; }
  .newsletter-input { width: 261px; height: 46px; background: var(--white); border: 0; }
  .newsletter-btn { width: 128px; height: 46px; background: var(--black); color: var(--white); font-size: 21px;
    font-weight: 600; display: flex; align-items: center; justify-content: center; }
  .copyright { position: absolute; left: 0; right: 0; top: 274px; text-align: center; font-size: 14px; font-weight: 600; }
</style>
</head>
<body>
  <header class="hero" role="img" aria-label="Red-tinted photo of a living room with a television">
    <div class="brand"><span class="brand-dot"></span>Plomzar</div>
    <h1 class="hero-title">Social Television</h1>
    <p class="hero-sub">Movies, Game Shows, News, And Everything On TV</p>
    <div class="hero-actions">
      <span class="btn-outline">Get the App</span>
      <span class="link-signup">Sign Up</span>
    </div>
    <div class="hero-phone" role="img" aria-label="Hand holding a phone showing the app's chat screen"></div>
  </header>

  <section class="tagline">Turn On Your TV and Join The Fans In Real Time</section>

  <section class="feature" style="top:728px">
    <div class="feature-media m1" role="img" aria-label="Stadium graphic for a live football broadcast"></div>
    <div class="feature-text"><h2 class="feature-title">Live Sports Chatrooms</h2><p class="feature-sub">Follow Your Favorite Teams</p></div>
  </section>
  <section class="feature" style="top:941px">
    <div class="feature-media m2" role="img" aria-label="Television screen showing a grid of show posters"></div>
    <div class="feature-text"><h2 class="feature-title">Reality TV Chatrooms</h2><p class="feature-sub">Don't Miss Your TV Shows Get Automatic Reminders</p></div>
  </section>
  <section class="feature" style="top:1164px">
    <div class="feature-media m3" role="img" aria-label="Person browsing on a smartphone"></div>
    <div class="feature-text"><h2 class="feature-title">Search and Follow</h2><p class="feature-sub">Sort Your TV Channels And Much More</p></div>
  </section>
  <section class="feature" style="top:1386px">
    <div class="feature-media m4" role="img" aria-label="Television on a white stand with a plant and game controller"></div>
    <div class="feature-text"><h2 class="feature-title">Social TV App</h2><p class="feature-sub">Can't Wait For Your Friends To Comment Back?</p></div>
  </section>

  <section class="invite" role="img" aria-label="Darkened photo of a living room with a TV and a plant">
    <h2 class="invite-title">Share and Invite</h2>
    <p class="invite-sub">Your Friends To Any TV Show</p>
    <span class="btn-solid">Get the App</span>
  </section>

  <footer class="footer">
    <div class="brand"><span class="brand-dot"></span>Plomzar</div>
    <p class="footer-address">1180 Harbor Ave, Fremont, CA 94536</p>
    <p class="footer-email">info@plomzar.com</p>
    <p class="newsletter-label">Get the latest update</p>
    <div class="newsletter"><span class="newsletter-input"></span><span class="newsletter-btn">Sign up</span></div>
    <p class="copyright">© 2017 Plomzar, Inc.</p>
  </footer>
</body>
</html>
```